Furniture Design Website Homepage

Brief as attached- Homepage Design

Silver Heron Furniture is a national retail emporium offering high quality, unique Scandinavian furniture, lighting and accessories. We are the market leader in this space and currently have 2 Showrooms – Melbourne & Sydney.

Most recently our business model has evolved from purely importing premium, one off vintage pieces to a more scalable model of representing brands and manufacturers exclusively out of Scandinavia. These partners manufacture today which ensures us of supply & quality.

We have now started to engage scandinavian designers and/or their families to re-introduce designs that have long gone out of production. These items are put back into production under the silver heron brand, and we own the world wide rights to them.

Please ensure you use the brief files attached and the catalogue images when creating the design.

Target Market(s)

Silver Heron Furniture - where beautiful Scandinavian design meets my modern Australian life.

We want our target audience to chose Scandinavian for their homes & for us to be their brand of choice.

The current perception is that we offer beautiful design but that it doesn’t suit everyone’s home / life / style.

Also that we are more expensive than most.

Industry/Entity Type

Retail

Requirements
Must have
• The colour scheme should be red and white as per the catalogue I attached. We like the look and feel of this site www.roomfondly.example

The furniture is more luxurious, so we need to target the upper market with a nice sleek look that makes the furniture look expensive.

```html
<!DOCTYPE html>
<html lang="en">
<head>
<meta charset="utf-8">
<title>Silver Heron Furniture – Home</title>
<link rel="stylesheet" href="https://fonts.googleapis.com/css2?family=Oswald:wght@300;400;500&family=Didact+Gothic&family=Arimo:wght@400;700&display=swap">
<style>
:root{
  --red:#ee1c1c;
  --red-dark:#c40000;
  --ink:#111;
  --grey-text:#888;
  --grey-mid:#777;
  --line:#c8c8c8;
  --panel:#f1f1f1;
  --panel-dark:#dcdcdc;
  --white:#fff;
  --teal:#1a7f73;
  --card:#7a8ea8;
}
*{box-sizing:border-box;margin:0;padding:0}
html,body{width:1182px;height:1200px;overflow:hidden;background:var(--white);font-family:Arimo,Arial,sans-serif;color:var(--ink)}
.page{position:absolute;left:138px;top:0;width:980px;height:1300px;transform:scale(.923);transform-origin:0 0;border-left:1px solid var(--line);border-right:1px solid var(--line)}
.abs{position:absolute}

/* header */
.brand{left:46px;top:62px;display:flex;align-items:center;gap:7px;font-family:Arimo,Arial,sans-serif;font-weight:700;font-size:23px;color:var(--ink);letter-spacing:-.3px;white-space:nowrap}
.brand-dot{width:13px;height:13px;border-radius:50%;background:var(--red)}
.tagline{left:220px;top:33px;font-family:Oswald,sans-serif;font-size:22px;line-height:34px;color:var(--ink);transform:scaleX(.85);transform-origin:0 0;white-space:nowrap}
.cart-title{left:865px;top:10px;font-family:"Didact Gothic",sans-serif;font-size:17px}
.btn-small{border:1px solid #999;border-radius:3px;background:linear-gradient(#fff,#e6e6e6);font-size:8px;font-weight:700;text-align:center;line-height:13px;white-space:nowrap}
.view-cart{left:910px;top:48px;width:58px;height:15px}
.secure{left:832px;top:70px;width:142px;height:24px;border-radius:12px;border:1px solid #aaa;background:linear-gradient(#f4f4f4,#cfcfcf);font-size:10px;font-weight:700;line-height:22px;padding-left:32px;white-space:nowrap}
.secure svg{position:absolute;left:10px;top:3px}
.nav{left:0;top:108px;height:24px;width:980px}
.nav a{position:absolute;top:0;height:23px;font-family:Arimo,Arial,sans-serif;font-size:12px;line-height:23px;text-decoration:none;text-align:center;color:var(--ink);white-space:nowrap}
.nav .tab{background:var(--red);color:#111;border-radius:2px 2px 0 0}
.header-shadow{left:0;top:132px;width:980px;height:9px;background:linear-gradient(#9a9a9a,#fff)}

/* sidebar */
.sidebar{left:0;top:145px;width:218px;height:983px;background:var(--panel)}
.search-title{left:0;top:146px;width:218px;height:26px;background:var(--red);color:#fff;font-size:16px;line-height:26px;padding-left:9px}
.search-input{left:4px;top:184px;width:105px;height:18px;border:1px solid #999;background:#fff}
.search-btn{left:114px;top:184px;width:99px;height:20px;border:1px solid #999;background:linear-gradient(#f8f8f8,#d8d8d8);font-size:11px;font-weight:700;text-align:center;line-height:18px}
.browse{left:8px;top:222px;width:130px;height:156px;background:#fff}
.browse li{list-style:none;font-size:12.5px;font-weight:700;height:25px;padding-left:5px;line-height:25px}
.filter{left:7px;top:382px;width:187px;height:284px;border:1px solid #aaa;background:#fff}
.filter-head{height:31px;background:var(--panel-dark);border-bottom:1px solid #aaa;font-size:12px;font-weight:700;line-height:31px;padding-left:7px}
.filter-row{position:absolute;left:8px;font-size:12px}
.select{position:absolute;left:89px;top:-6px;width:89px;height:22px;border:1px solid #999;background:#fff}
.select::after{content:"▾";position:absolute;right:0;top:0;width:12px;height:20px;border-left:1px solid #999;font-size:8px;line-height:20px;text-align:center}
.filter-foot{position:absolute;left:0;bottom:0;width:185px;height:38px;background:var(--panel-dark);border-top:1px solid #aaa}
.pill-red{position:absolute;left:10px;top:6px;width:149px;height:24px;border-radius:12px;background:linear-gradient(#ff3b3b,var(--red-dark));color:#fff;font-size:13px;text-align:center;line-height:24px}
.keep{left:8px;top:700px;width:183px;height:165px;background:#fff}
.keep h3{position:absolute;left:10px;top:4px;font-family:"Didact Gothic",sans-serif;font-weight:400;font-size:19px;white-space:nowrap}
.keep p{position:absolute;left:10px;top:32px;width:100px;font-size:12px;font-weight:700;color:var(--grey-text);line-height:15px}
.keep-art{position:absolute;left:106px;top:36px;width:66px;height:82px;background:linear-gradient(#fafafa,#e2e2e2)}
.pill-grey{position:absolute;left:8px;top:127px;width:127px;height:20px;border-radius:10px;border:1px solid #999;background:linear-gradient(#fafafa,#cfcfcf);font-size:11px;text-align:center;line-height:18px}
.privacy{position:absolute;left:10px;top:157px;font-family:"Didact Gothic",sans-serif;font-size:12px}
.testi-title{left:0;top:900px;width:178px;text-align:center;font-family:"Didact Gothic",sans-serif;font-size:19px}
.testi-art{left:26px;top:937px;width:138px;height:153px;background:linear-gradient(#fff,#e4e4e4)}
.testi-link{left:0;top:1095px;width:194px;text-align:center;font-family:"Didact Gothic",sans-serif;font-size:12px}

/* main */
.heading{left:230px;top:150px;font-family:Oswald,sans-serif;font-weight:500;font-size:36px;letter-spacing:.5px;transform:scaleX(.9);transform-origin:0 0}
.intro{left:230px;top:198px;width:735px;font-size:14px;line-height:17px;color:var(--grey-text)}
.slideshow{left:222px;top:242px;width:451px;height:369px;border:1px solid #ccc;background:#fff}
.slide-art{position:absolute;left:50px;top:0;width:350px;height:367px;background:radial-gradient(ellipse at 50% 55%,#d4d4d4 0%,#f3f3f3 45%,#fff 70%)}
.slide-caption{position:absolute;left:0;top:330px;width:451px;text-align:center;font-family:"Didact Gothic",sans-serif;font-size:23px;letter-spacing:1.5px}
.cat{left:680px;width:292px;height:113px;border:1px solid #aaa;border-radius:14px;background:linear-gradient(#fbfbfb,#e6e6e6);overflow:hidden}
.cat-art{position:absolute;left:8px;top:0;width:120px;height:111px}
.cat-title{position:absolute;left:152px;top:52px;font-family:"Didact Gothic",sans-serif;font-size:25px;transform:translateY(-50%)}
.cat-link{position:absolute;left:152px;top:84px;font-family:"Didact Gothic",sans-serif;font-size:16px;color:var(--grey-mid);transform:translateY(-50%);white-space:nowrap}
.rec-title{left:229px;top:646px;display:flex;align-items:baseline;gap:6px;font-size:17px}
.rec-title b{font-weight:700;font-size:19px}
.rec-title span{font-family:"Didact Gothic",sans-serif}
.rec-box{left:227px;top:678px;width:742px;height:241px;border:1px solid #aaa;border-radius:14px;background:linear-gradient(#fafafa,#ececec)}
.product{position:absolute;top:13px;width:168px;height:218px}
.product-art{position:absolute;left:0;top:0;width:168px;height:161px}
.product-name{position:absolute;left:0;top:161px;width:168px;height:18px;background:var(--grey-mid);color:#fff;font-size:12px;font-weight:700;line-height:18px;padding-left:6px;white-space:nowrap;overflow:hidden}
.more{position:absolute;right:6px;top:185px;font-size:12px;color:var(--grey-text)}
.price{position:absolute;left:6px;top:204px;font-size:12px;color:var(--grey-mid)}
.add{position:absolute;right:8px;top:203px;width:58px;height:15px}
.news{left:232px;top:949px;width:729px;height:181px;border:1px solid #999;background:#fff}
.news-head{height:35px;background:var(--panel-dark);border-bottom:1px solid #999;text-align:center;font-family:Oswald,sans-serif;font-weight:300;font-size:17px;line-height:33px}
.news-text{position:absolute;left:15px;top:48px;font-size:12px;color:#444}
.field-label{position:absolute;font-size:12px}
.field{position:absolute;width:153px;height:22px;border:1px solid #999;background:#fff}
.news-promo{position:absolute;left:533px;top:47px;width:168px;height:65px;background:linear-gradient(#fff 0,#fff 40%,var(--red) 40%);border:1px solid var(--red-dark)}
.news-promo .env{position:absolute;left:6px;top:6px;width:54px;height:50px;background:linear-gradient(135deg,#bfdcf5,#5a8fc9)}
.news-promo .a{position:absolute;left:70px;top:4px;font-family:"Didact Gothic",sans-serif;font-size:17px}
.news-promo .b{position:absolute;left:68px;top:26px;color:#fff;font-weight:700;font-size:15px}
.news-promo .c{position:absolute;left:83px;top:46px;color:#fff;font-size:10px}
.news-privacy{position:absolute;left:531px;top:120px;font-size:12px;color:var(--grey-mid)}
.news-foot{position:absolute;left:0;bottom:0;width:727px;height:40px;background:var(--panel-dark);border-top:1px solid #999}
.send{position:absolute;left:658px;top:7px;width:58px;height:25px;border:1px solid #999;background:linear-gradient(#fff,#ddd);font-size:12px;text-align:center;line-height:23px}

/* footer */
.pay-label{left:28px;top:1146px;font-family:"Didact Gothic",sans-serif;font-size:14px;color:var(--grey-mid)}
.pay-name{left:28px;top:1166px;font-family:"Didact Gothic",sans-serif;font-size:27px;color:var(--teal);white-space:nowrap}
.card{width:37px;height:24px;border-radius:3px;background:var(--card)}
.links{left:248px;top:1146px;width:718px}
.col{position:absolute;top:0}
.col li{list-style:none;height:30px;font-size:12px;color:#555;line-height:16px;white-space:nowrap}
.col li:first-child{font-size:12.5px}
.rule{position:absolute;left:246px;width:718px;height:1px;background:#999}
</style>
</head>
<body>
<div class="page">

  <!-- header -->
  <div class="abs brand"><span class="brand-dot"></span>silver heron</div>
  <div class="abs tagline">The Best of Modern and Classic<br>Scandinavian Design</div>
  <div class="abs cart-title">Shopping Cart</div>
  <div class="abs btn-small view-cart">View Cart</div>
  <div class="abs secure">
    <svg width="14" height="17" viewBox="0 0 14 17"><path d="M3 8V5a4 4 0 0 1 8 0v3" fill="none" stroke="#777" stroke-width="2"/><rect x="1" y="8" width="12" height="9" rx="1" fill="#888"/></svg>
    SECURE SHOPPING
  </div>
  <nav class="abs nav">
    <a style="left:47px">ABOUT US</a>
    <a class="tab" style="left:121px;width:172px">FURNITURE RESTORATION</a>
    <a class="tab" style="left:297px;width:60px">MEDIA</a>
    <a class="tab" style="left:360px;width:44px">FAQ</a>
    <a class="tab" style="left:408px;width:99px">MAILING LIST</a>
    <a class="tab" style="left:510px;width:54px">BLOG</a>
    <a class="tab" style="left:567px;width:94px">SITE SEARCH</a>
    <a class="tab" style="left:664px;width:97px">CONTACT US</a>
    <a class="tab" style="left:764px;width:121px">ACCOUNT/LOGIN</a>
  </nav>
  <div class="abs header-shadow"></div>

  <!-- sidebar -->
  <aside>
    <div class="abs sidebar"></div>
    <div class="abs search-title">Product Search</div>
    <div class="abs search-input"></div>
    <div class="abs search-btn">Search</div>
    <ul class="abs browse">
      <li>Browse Our Range</li><li>Furniture</li><li>Furniture</li><li>Accessories</li><li>Lighting</li><li>Fabrics</li>
    </ul>
    <div class="abs filter">
      <div class="filter-head">View Products By Type</div>
      <div class="filter-row" style="top:45px">Room:<span class="select"></span></div>
      <div class="filter-row" style="top:78px">Furniture:<span class="select"></span></div>
      <div class="filter-row" style="top:111px">Designers:<span class="select"></span></div>
      <div class="filter-row" style="top:144px">Brands:<span class="select"></span></div>
      <div class="filter-row" style="top:177px">Accessories:<span class="select"></span></div>
      <div class="filter-foot"><div class="pill-red">Find Product</div></div>
    </div>
    <div class="abs keep">
      <h3>Keep Up To Date</h3>
      <p>Discover exclusive offers, products previews and much more</p>
      <div class="keep-art" role="img" aria-label="Figure carrying an envelope"></div>
      <div class="pill-grey">Join Our Newsletter</div>
      <div class="privacy">We value your privacy</div>
    </div>
    <div class="abs testi-title">Testimonials</div>
    <div class="abs testi-art" role="img" aria-label="Figure holding a large red tick"></div>
    <div class="abs testi-link">View more Testimonials</div>
  </aside>

  <!-- main -->
  <main>
    <h1 class="abs heading">HEADING</h1>
    <p class="abs intro">Lorem ipsum dolor sit amet, consectetur adipiscing elit. Nullam lacinia nisi sed purus molestie eget viverra tortor placerat. Mauris ultricies ullamcorper sapien, nec dignissim odio mattis in. Morbi vulputate posuere.</p>

    <div class="abs slideshow">
      <div class="slide-art" role="img" aria-label="Silver pendant lamp photograph"></div>
      <div class="slide-caption">(Slideshow image 6)</div>
    </div>

    <div class="abs cat" style="top:247px">
      <div class="cat-art" role="img" aria-label="Black leather armchair" style="background:linear-gradient(#3a3a3a,#7a5a3a)"></div>
      <div class="cat-title">Furniture</div><div class="cat-link">View Collection &gt;</div>
    </div>
    <div class="abs cat" style="top:372px">
      <div class="cat-art" role="img" aria-label="Yellow wall hooks" style="background:radial-gradient(circle at 45% 50%,#f2dc2a 0,#f6ef9a 35%,transparent 70%)"></div>
      <div class="cat-title">Accesories</div><div class="cat-link">View Collection &gt;</div>
    </div>
    <div class="abs cat" style="top:494px">
      <div class="cat-art" role="img" aria-label="Glass bulb pendant" style="background:radial-gradient(ellipse at 50% 80%,#d0d0d0 0,#eee 35%,transparent 60%)"></div>
      <div class="cat-title" style="left:162px">Lighting</div><div class="cat-link" style="left:160px">View Collection &gt;</div>
    </div>

    <div class="abs rec-title"><b>silver heron</b><span>Recommends</span></div>
    <section class="abs rec-box">
      <div class="product" style="left:17px">
        <div class="product-art" role="img" aria-label="Green rocking chair" style="background:linear-gradient(#fff,#9fcf3c 40%,#d8d8d8)"></div>
        <div class="product-name">Ray Rocker</div><div class="more">MORE INFO</div><div class="price">$2,299</div><div class="btn-small add">Add to Cart</div>
      </div>
      <div class="product" style="left:197px">
        <div class="product-art" role="img" aria-label="Red dome pendant lamp" style="background:radial-gradient(ellipse at 50% 40%,#e0201c 0,#b5100d 45%,#fff 70%)"></div>
        <div class="product-name">Bloom Pendant – Large</div><div class="more">MORE INFO</div><div class="price">$2,299</div><div class="btn-small add">Add to Cart</div>
      </div>
      <div class="product" style="left:377px">
        <div class="product-art" role="img" aria-label="Wooden dining chair" style="background:linear-gradient(#fff,#6b4326 50%,#3a2414)"></div>
        <div class="product-name">Alva Dining Chair – Oak</div><div class="more">MORE INFO</div><div class="price">$2,299</div><div class="btn-small add">Add to Cart</div>
      </div>
      <div class="product" style="left:558px">
        <div class="product-art" role="img" aria-label="Chrome table lamp" style="background:radial-gradient(ellipse at 35% 40%,#eee 0,#444 40%,#fff 65%)"></div>
        <div class="product-name">Bloom – Table Lamp</div><div class="more">MORE INFO</div><div class="price">$2,299</div><div class="btn-small add">Add to Cart</div>
      </div>
    </section>

    <section class="abs news">
      <div class="news-head">Join Our Newsletter</div>
      <div class="news-text">Discover exclusive offers, product reviews, information on sales and much more!</div>
      <div class="field-label" style="left:8px;top:80px">Name:</div><div class="field" style="left:57px;top:75px"></div>
      <div class="field-label" style="left:293px;top:80px">Email:</div><div class="field" style="left:357px;top:75px;width:138px"></div>
      <div class="field-label" style="left:8px;top:113px">State:</div><div class="field" style="left:57px;top:108px"><span class="select" style="left:-1px;top:-1px;width:153px"></span></div>
      <div class="field-label" style="left:293px;top:113px">Postcode:</div><div class="field" style="left:357px;top:108px;width:138px"></div>
      <div class="news-promo">
        <div class="env" role="img" aria-label="Blue envelope"></div>
        <div class="a">Join Our</div><div class="b">Newsletter</div><div class="c">Sign up now ▸</div>
      </div>
      <div class="news-privacy">We value your privacy</div>
      <div class="news-foot"><div class="send">Send</div></div>
    </section>
  </main>

  <!-- footer -->
  <footer>
    <div class="abs pay-label">Secure Online Shopping</div>
    <div class="abs pay-name">SafeCheckout</div>
    <div class="abs card" style="left:27px;top:1213px"></div>
    <div class="abs card" style="left:73px;top:1213px"></div>
    <div class="abs card" style="left:119px;top:1213px"></div>
    <div class="abs card" style="left:166px;top:1213px"></div>
    <div class="abs card" style="left:27px;top:1247px"></div>
    <div class="abs card" style="left:73px;top:1247px"></div>
    <div class="abs card" style="left:121px;top:1247px"></div>
    <div class="abs links">
      <ul class="col" style="left:0"><li>OUR RANGES</li><li>Specials</li><li>Leather sofas</li><li>Fabric sofas</li><li>Leather/Fabric sofas</li></ul>
      <ul class="col" style="left:169px"><li>ABOUT US</li><li>Meet the designers</li><li>Advertising</li><li>Latest brochure</li></ul>
      <ul class="col" style="left:359px"><li>NEED HELP?</li><li>Contact us</li><li>Orders</li><li>FAQs</li></ul>
    </div>
    <div class="rule" style="top:1198px"></div>
    <div class="rule" style="top:1231px"></div>
    <div class="rule" style="top:1261px"></div>
    <div class="rule" style="top:1291px"></div>
  </footer>
</div>
</body>
</html>
```